Ciel doux

Hello,
I’m a designer sunglasses reatail Store owner in Montreal, Quebec.

Looking for something modern, fresh with a trendy appeal.

Will send my logo.
Thank you.

Store

```html
<!DOCTYPE html>
<html lang="fr">
<head>
<meta charset="utf-8">
<title>Ciel doux – carte de visite</title>
<link rel="stylesheet" href="https://fonts.googleapis.com/css2?family=Open+Sans:wght@400;600;700&display=swap">
<style>
  :root {
    --page: #e7e3df;
    --card-top: #f3f1ee;
    --card-top-edge: #e6e2dd;
    --brand-red: #a3223a;
    --brand-red-deep: #861629;
    --ink: #2e2a2a;
    --on-red: #f6e6e9;
    --on-red-soft: rgba(246, 226, 230, 0.72);
  }
  * { box-sizing: border-box; margin: 0; padding: 0; }
  html, body {
    width: 1200px; height: 970px; overflow: hidden;
    background: var(--page);
    font-family: "Open Sans", sans-serif;
  }
  .business-card {
    position: absolute; left: 100px; top: 202px;
    width: 1000px; height: 565px;
    background: linear-gradient(180deg, var(--card-top), var(--card-top-edge));
    box-shadow: 0 14px 40px rgba(60, 40, 40, 0.18);
    overflow: hidden;
  }
  .brand-name {
    position: absolute; left: 82px; top: 78px;
    display: flex; align-items: center; gap: 14px;
    font-size: 40px; font-weight: 600; color: var(--brand-red);
    letter-spacing: 1px;
  }
  .brand-dot {
    width: 26px; height: 26px; border-radius: 50%;
    background: var(--brand-red);
  }
  .person {
    position: absolute; left: 175px; top: 240px;
  }
  .person-name {
    font-size: 32px; font-weight: 700; color: var(--brand-red);
    line-height: 1.2;
  }
  .person-role {
    font-size: 23px; font-weight: 400; color: var(--ink);
    margin-top: 4px;
  }
  .contact-band {
    position: absolute; left: 0; right: 0; top: 329px; bottom: 0;
    background: linear-gradient(90deg, var(--brand-red) 0%, var(--brand-red-deep) 100%);
  }
  .band-circle {
    position: absolute; right: -90px; top: -20px;
    width: 330px; height: 330px; border-radius: 50%;
    background: rgba(255, 255, 255, 0.12);
  }
  .address {
    position: absolute; left: 175px; top: 26px;
    font-size: 23px; line-height: 34px; color: var(--on-red);
  }
  .contact-list {
    position: absolute; left: 175px; top: 112px;
    list-style: none;
  }
  .contact-list li {
    display: flex; align-items: center; gap: 16px;
    font-size: 22px; line-height: 34px; color: var(--on-red-soft);
  }
  .contact-list svg { width: 20px; height: 20px; flex: none; }
</style>
</head>
<body>
  <main class="business-card">
    <div class="brand-name"><span class="brand-dot"></span>CIEL DOUX</div>

    <section class="person">
      <h1 class="person-name">Léa Marchand</h1>
      <p class="person-role">Gérante</p>
    </section>

    <section class="contact-band">
      <div class="band-circle"></div>
      <p class="address">48 Rue Laurier Ouest<br>Montréal, QC H2V 2K3</p>
      <ul class="contact-list">
        <li>
          <svg viewBox="0 0 20 20" aria-hidden="true"><path d="M5 2l3 4-2 2c1 2.5 3.5 5 6 6l2-2 4 3-2 3C9 18 2 11 2 4z" fill="var(--on-red)"/></svg>
          +1 514 555 0142
        </li>
        <li>
          <svg viewBox="0 0 20 20" aria-hidden="true"><rect x="2" y="5" width="16" height="11" rx="1" fill="var(--on-red)"/><path d="M2.5 5.5L10 11l7.5-5.5" stroke="var(--brand-red)" stroke-width="1.5" fill="none"/></svg>
          bonjour@cieldoux.ca
        </li>
        <li>
          <svg viewBox="0 0 20 20" aria-hidden="true"><circle cx="10" cy="10" r="8" fill="none" stroke="var(--on-red)" stroke-width="1.6"/><ellipse cx="10" cy="10" rx="3.5" ry="8" fill="none" stroke="var(--on-red)" stroke-width="1.4"/><path d="M2 10h16" stroke="var(--on-red)" stroke-width="1.4"/></svg>
          www.cieldoux.ca
        </li>
      </ul>
    </section>
  </main>
</body>
</html>
```